Security Officer Training Certifications POSTCARD

We need Post Card Design
-Front and Back
-In Compliance with TORLEN HUB for upload!
-For Oversized and Jumbo Size Cards (torlen hubs)
Our Company:
www.ashworthmaplebrookinstitute.org (FOR IDEAS)
We provide Corporate Security Officer/Criminal Justice/Police Tactics Training for Private Companies that have a security department and officers.
We provide:
Handcuffing certifications
Pepper Spray
Compliance Training
Instructor Training
California Guard Card
Our Card to display powerful image for a Security Officer Department
Traits in Pic and Deigns
VALUE
COMPETITIVE EDGE
PROFESSIONAL GROWTH
QUALITY
PROFICIENT/EFFECTIVE SECURITY OFFICERS
TACTICAL OFFICERS
PROFESSIONALISM
EXPERTS
INDUSTRY LEADERS
READINESS
FRONT DESIGN TO BE VERY CATCH AND ATTRACTIVE!
-Please put the images of lawn enforcement, security guards, public safety department in the FRONT
BACK OF THE CARD DESIGN
-Please put our Services/Menu, CREATIVE and CATCHY, in columns and with vivid colors.

```html
<!DOCTYPE html>
<html lang="en">
<head>
<meta charset="utf-8">
<title>Security Officer Training Postcard</title>
<link rel="stylesheet" href="https://fonts.googleapis.com/css2?family=Oswald:wght@500;600;700&family=Lato:wght@400;700&display=swap">
<style>
  :root {
    --stage: #3c3c3e;
    --card: #ffffff;
    --brand-red: #9b1b22;
    --band-red: #971a20;
    --ink-gray: #4a4a4a;
    --body-gray: #5a5a5a;
    --silver: #c9c9c9;
    --navy: #1c2233;
    --stamp: #000000;
    --rule: #1a1a1a;
  }
  * { box-sizing: border-box; margin: 0; padding: 0; }
  html, body { width: 800px; height: 1200px; overflow: hidden; }
  body { background: var(--stage); position: relative; font-family: "Lato", sans-serif; }

  .postcard { position: absolute; left: 51px; width: 699px; height: 465px; background: var(--card); overflow: hidden; }
  .postcard--front { top: 122px; background: linear-gradient(100deg, #e6e6e6 0%, #ffffff 30%, #ffffff 100%); }
  .postcard--back { top: 614px; }

  .front__title { position: absolute; left: 34px; top: 65px; font-family: "Oswald", sans-serif; font-weight: 700;
    font-size: 57px; line-height: 1; color: var(--brand-red); letter-spacing: -0.5px; transform: scaleX(0.93); transform-origin: left; }
  .front__subtitle { position: absolute; left: 34px; top: 124px; font-family: "Oswald", sans-serif; font-weight: 600;
    font-size: 23px; line-height: 1; color: var(--ink-gray); transform: scaleX(0.9); transform-origin: left; white-space: nowrap; }
  .front__tagline { position: absolute; left: 34px; top: 157px; font-family: "Oswald", sans-serif; font-weight: 600;
    font-size: 30px; line-height: 1; color: var(--ink-gray); transform: scaleX(0.9); transform-origin: left; white-space: nowrap; }

  .front__band { position: absolute; left: 0; top: 214px; width: 400px; height: 118px; background: var(--band-red); }
  .front__band-text { position: absolute; left: 34px; top: 228px; width: 340px; color: #fff; font-size: 16.5px; line-height: 21.6px; }

  .front__call { position: absolute; left: 34px; top: 346px; font-weight: 700; font-size: 29px; color: var(--brand-red); white-space: nowrap; }
  .front__area { position: absolute; left: 34px; top: 386px; font-weight: 700; font-size: 15px; line-height: 20px; color: var(--body-gray); }

  .front__photo { position: absolute; left: 380px; top: 0; width: 319px; height: 465px;
    background: linear-gradient(90deg, rgba(255,255,255,0) 0%, #2a3147 22%, #1c2233 50%, #f2f2f2 52%, #1c2233 60%, #232a3e 100%); }

  .back__strip { position: absolute; left: 0; width: 210px; height: 30px; background: linear-gradient(90deg, #bfbfbf, #ffffff); }
  .back__strip--top { top: 0; }
  .back__strip--bottom { bottom: 0; }
  .back__panel { position: absolute; left: 0; top: 30px; width: 301px; height: 404px; background: var(--band-red);
    border-radius: 0 34px 34px 0; color: #fff; padding: 24px 0 0 27px; }
  .back__heading { font-weight: 700; font-size: 14.5px; line-height: 20.8px; }
  .services { list-style: none; margin-bottom: 25px; }
  .services li { position: relative; padding-left: 21px; font-size: 14.5px; line-height: 20.8px; font-weight: 700; letter-spacing: -0.2px; }
  .services li::before { content: ""; position: absolute; left: 8px; top: 7px; width: 7px; height: 7px; border-radius: 50%; background: #fff; }

  .back__badges { position: absolute; left: 0; top: 0; }
  .back__stamp { position: absolute; left: 582px; top: 28px; width: 87px; height: 87px; background: var(--stamp); }
  .address-line { position: absolute; left: 409px; width: 260px; height: 1.5px; background: var(--rule); }
</style>
</head>
<body>

<section class="postcard postcard--front">
  <div class="front__photo" role="img" aria-label="Photo of two uniformed security officers standing back to back with arms crossed"></div>
  <h1 class="front__title">SECURITY GUARD</h1>
  <p class="front__subtitle">Training in Los Angeles California</p>
  <p class="front__tagline">GUARD CARD SPECIALISTS</p>
  <div class="front__band"></div>
  <p class="front__band-text">We provide Corporate Security Officer/ Criminal Justice/Police Tactics Training for Private Companies that have a security department and officers.</p>
  <p class="front__call">Call Now (555) 014-2290</p>
  <p class="front__area">City Of Commerce, L.A and East L.A cities<br>2180 E. Harlow Ave, Commerce, CA 90040</p>
</section>

<section class="postcard postcard--back">
  <div class="back__strip back__strip--top"></div>
  <div class="back__strip back__strip--bottom"></div>
  <div class="back__panel">
    <p class="back__heading">We provide:</p>
    <ul class="services">
      <li>Handcuffing certifications</li>
      <li>Pepper Spray</li>
      <li>Compliance Training</li>
      <li>Instructor Training</li>
      <li>California Guard Card</li>
    </ul>
    <ul class="services">
      <li>Value</li>
      <li>Competitive Edge</li>
      <li>Professional Growth</li>
      <li>Quality</li>
      <li>Proficient/effective Security Officers</li>
      <li>Tactical Officers</li>
      <li>Professionalism</li>
      <li>Experts</li>
      <li>Industry Leaders</li>
      <li>Readiness</li>
    </ul>
  </div>

  <svg class="back__badges" width="699" height="465" viewBox="0 0 699 465" aria-hidden="true">
    <defs>
      <linearGradient id="silver-fill" x1="0" y1="0" x2="1" y2="1">
        <stop offset="0" stop-color="#eeeeee"/>
        <stop offset="1" stop-color="#a9a9a9"/>
      </linearGradient>
    </defs>
    <ellipse cx="387" cy="174" rx="70" ry="102" fill="url(#silver-fill)"/>
    <path d="M461 86 H565 V130 Q565 160 513 168 Q461 160 461 130 Z" fill="#b3262c"/>
    <path d="M477 182 H541 V230 Q541 262 509 276 Q477 262 477 230 Z" fill="#c4c4c4"/>
    <rect x="561" y="178" width="88" height="100" fill="#0d1a2e"/>
  </svg>

  <div class="back__stamp"></div>
  <div class="address-line" style="top:310px"></div>
  <div class="address-line" style="top:354px"></div>
  <div class="address-line" style="top:398px"></div>
</section>

</body>
</html>
```